Biodegradable box for eco-friendly bamboo cotton buds

I am looking for a design on a box holding 200 bamboo cotton buds. The box opens like a matchstick box and is made from recycled card. It's to sell online and at markets, maybe also supermarkets.
It's the second product my company, Verdalin, will sell, so I would like a design that I can replicate on other product packaging in the future.
You can see more about Verdalin on my website www.verdalin.org or facebook and instagram @verdalinqatar.
Please see below the box dimensions from the supplier and a photo. Also, some ideas I have had using Canva. I would like to see the green strip go all the way round the box. I like the font. The cotton bud logo is copyrighted - I like the style, but a new one would need to be created.

Target Market(s)

Eco-conscious consumers - expats and locals - in Qatar

Industry/Entity Type

Retail

Font styles to use
Other font styles liked:
• special elite

Colors
cadf82
acd037
eaf2ce
9ccb3b

Requirements
Must have
• an environmentally-friendly focus

```html
<!DOCTYPE html>
<html lang="en">
<head>
<meta charset="utf-8">
<title>Verdalin – Bamboo Cotton Buds Box Dieline</title>
<link rel="stylesheet" href="https://fonts.googleapis.com/css2?family=Special+Elite&family=Montserrat:wght@400&display=swap">
<style>
:root{
  --bg:#a7a8ac;
  --cream:#eaf2ce;
  --lime:#acd037;
  --lime-soft:#cadf82;
  --bud-tint:rgba(202,223,130,.45);
  --ink:#1d1d1b;
}
*{box-sizing:border-box;margin:0;padding:0}
html,body{width:1200px;height:1200px;overflow:hidden;background:var(--bg)}
.canvas{position:relative;width:1200px;height:1200px}
.face{position:absolute;background:var(--cream);overflow:hidden}
.strip{position:absolute;top:0;right:0;height:100%;background:var(--lime)}
.type{font-family:"Special Elite",monospace;color:var(--ink);position:absolute}
.brand{position:absolute;font-family:"Montserrat",sans-serif;font-weight:400;color:var(--ink);text-align:center;width:100%;left:0}
.bud-art{position:absolute;background:radial-gradient(ellipse at center,var(--bud-tint) 0%,rgba(202,223,130,.18) 55%,rgba(234,242,206,0) 75%)}
.mascot-art{position:absolute;border-radius:50%;background:radial-gradient(circle,rgba(202,223,130,.55) 0%,rgba(202,223,130,.25) 55%,rgba(172,208,55,0) 72%)}
.title-main{font-size:66px;line-height:1;letter-spacing:0}
.title-sub{font-size:38px;line-height:1}
.count{position:absolute;left:0;background:var(--lime);border-radius:0 10px 10px 0;font-family:"Special Elite",monospace;color:var(--ink)}
.count small{font-size:.7em}
.claims{font-size:15px;line-height:19px}
.small{font-size:10px;line-height:13px}

.front{left:95px;top:120px;width:449px;height:382px}
.flap{left:95px;top:570px;width:449px;height:185px}
.side{left:631px;top:126px;width:375px;height:1007px}
.side .strip{width:112px;height:950px}
.handle-dot{display:inline-block;width:11px;height:11px;border-radius:50%;background:var(--ink);vertical-align:-1px;margin-right:4px}
.cert{display:inline-block;width:14px;height:10px;background:var(--ink);margin-top:4px}
</style>
</head>
<body>
<div class="canvas">

  <section class="face front">
    <div class="bud-art" role="img" aria-label="Faint crossed bamboo cotton buds illustration" style="left:30px;top:135px;width:340px;height:190px"></div>
    <div class="type title-main" style="left:28px;top:28px">bamboo</div>
    <div class="type title-sub" style="left:30px;top:96px">cotton buds</div>
    <div class="count" style="top:316px;width:131px;height:40px;font-size:29px;line-height:42px;padding-left:26px">200<small>ea</small></div>
    <div class="strip" style="width:134px">
      <div class="mascot-art" role="img" aria-label="Faint brand mascot decoration" style="left:18px;top:22px;width:100px;height:100px"></div>
      <div class="brand" style="top:330px;font-size:20px">Verdalin</div>
    </div>
  </section>

  <section class="face flap">
    <div class="bud-art" role="img" aria-label="Faint crossed bamboo cotton buds illustration" style="left:-20px;top:-10px;width:340px;height:150px"></div>
    <div class="type claims" style="left:27px;top:124px">100% Biodegradable buds<br>100% Biodegradable packaging</div>
    <div class="strip" style="width:134px">
      <div class="brand" style="top:130px;font-size:20px">Verdalin</div>
    </div>
  </section>

  <section class="face side">
    <div class="bud-art" role="img" aria-label="Faint bamboo cotton buds illustration" style="left:-20px;top:-20px;width:290px;height:100px"></div>
    <div class="bud-art" role="img" aria-label="Faint crossed bamboo cotton buds illustration" style="left:20px;top:265px;width:270px;height:150px"></div>
    <div class="bud-art" role="img" aria-label="Faint bamboo cotton buds illustration" style="left:-20px;top:470px;width:290px;height:120px"></div>
    <div class="bud-art" role="img" aria-label="Faint bamboo cotton buds illustration" style="left:-20px;top:630px;width:280px;height:120px"></div>

    <div class="type" style="left:23px;top:86px;font-size:12px;line-height:17px">Find more products at:<br>www.verdalin.org<br><span class="handle-dot"></span>@verdalinqatar</div>
    <div class="type title-main" style="left:23px;top:178px;font-size:56px">bamboo</div>
    <div class="type title-sub" style="left:25px;top:233px;font-size:33px">cotton buds</div>
    <div class="count" style="top:419px;width:110px;height:34px;font-size:24px;line-height:36px;padding-left:22px">200<small>ea</small></div>
    <div class="type" style="left:23px;top:577px;font-size:12.5px;line-height:16px">100% Biodegradable buds<br>100% Biodegradable packaging</div>
    <div class="type small" style="left:23px;top:707px;width:222px">Cotton buds have many uses, cleaning your ears is not one of them!<br><br>Ear wax is your ear's natural way of cleaning itself. Putting buds in disrupts this process and damages the ear canal.<br><br>Never put anything smaller than your elbow in your ear!</div>
    <div class="type" style="left:23px;top:908px;font-size:12px;line-height:15px">MADE IN CHINA<br><span class="cert" role="img" aria-label="Certification mark"></span></div>

    <div class="strip">
      <div class="brand" style="top:100px;font-size:17px">Verdalin</div>
      <div class="mascot-art" role="img" aria-label="Faint brand mascot decoration" style="left:16px;top:172px;width:80px;height:80px"></div>
      <div class="brand" style="top:421px;font-size:17px">Verdalin</div>
      <div class="brand" style="top:576px;font-size:17px">Verdalin</div>
      <div class="mascot-art" role="img" aria-label="Faint brand mascot decoration" style="left:16px;top:647px;width:80px;height:80px"></div>
      <div class="brand" style="top:896px;font-size:17px">Verdalin</div>
    </div>
  </section>

</div>
</body>
</html>
```